BRIM Outreach Partners Business Card Rebrand

Hello Designers! We are looking for help designing our new business card to go in conjunction with our company rebrand. Unfortunately, we have an event mid June that requires we get these printed ASAP (before our new website is launched.) We have a mostly complete Brand Book which I have uploaded to this request for your reference to company information, style, fonts. I've also enclosed our logo file in .eps & .jpg. Attached is a sample business card my boss liked but said was "too simple." I made it in Canva and do not profess to be a designer. NOT FOR DESIGN REFERENCE, ONLY FOR CONTEXT Here is what our old website looks like: https://brimoutreachpartners.com/.

```html
<!DOCTYPE html>
<html lang="en">
<head>
<meta charset="UTF-8">
<title>BRIM Outreach Partners — Business Card</title>
<link href="https://fonts.googleapis.com/css2?family=Montserrat:wght@500;700&family=Arimo:wght@400;700&display=swap" rel="stylesheet">
<style>
  :root {
    --backdrop: #2f2f2f;
    --brand-blue: #4db3e6;
    --ink: #0d0d0d;
    --paper: #ffffff;
    --divider: #111111;
  }
  * { box-sizing: border-box; margin: 0; padding: 0; }
  html, body {
    width: 1200px; height: 689px; overflow: hidden;
    background: var(--backdrop);
  }
  .canvas {
    position: relative; width: 1200px; height: 689px;
    display: flex; align-items: center; justify-content: center; gap: 40px;
  }
  .card {
    width: 520px; height: 298px; border-radius: 18px; overflow: hidden;
    position: relative;
  }
  /* Front */
  .card-front {
    background: var(--brand-blue);
    display: flex; flex-direction: column; align-items: center; justify-content: center;
  }
  .front-mark {
    display: flex; align-items: center; gap: 16px;
  }
  .front-mark .dot {
    width: 70px; height: 70px; border-radius: 50%; background: var(--ink); flex: none;
  }
  .front-mark .name {
    font-family: "Montserrat", sans-serif; font-weight: 700; font-size: 26px;
    color: var(--ink); line-height: 1.1; width: 220px;
  }
  .front-url {
    position: absolute; bottom: 34px; left: 0; right: 0; text-align: center;
    font-family: "Arimo", sans-serif; font-size: 13px; color: var(--ink);
  }
  /* Back */
  .card-back { display: flex; background: var(--paper); }
  .back-logo {
    width: 47%; background: var(--paper);
    display: flex; align-items: center; justify-content: center; gap: 10px;
    padding: 0 18px;
  }
  .back-logo .dot {
    width: 42px; height: 42px; border-radius: 50%; background: var(--brand-blue); flex: none;
  }
  .back-logo .name {
    font-family: "Montserrat", sans-serif; font-weight: 700; font-size: 19px;
    color: var(--ink); line-height: 1.1;
  }
  .back-divider { width: 3px; background: var(--divider); flex: none; }
  .back-info {
    flex: 1; background: var(--brand-blue); color: var(--paper);
    font-family: "Arimo", sans-serif; padding: 64px 18px 0 24px;
  }
  .person-name { font-size: 21px; font-weight: 700; white-space: nowrap; }
  .person-title { font-size: 11px; margin-top: 2px; }
  .location { font-size: 11px; margin-top: 20px; }
  .contact-list { list-style: none; margin-top: 6px; }
  .contact-list li {
    display: flex; align-items: center; gap: 8px; font-size: 11px; line-height: 1.55;
    white-space: nowrap;
  }
  .contact-list svg { width: 10px; height: 10px; fill: var(--paper); flex: none; }
</style>
</head>
<body>
<main class="canvas">
  <section class="card card-front">
    <div class="front-mark">
      <span class="dot"></span>
      <span class="name">BRIM Outreach Partners</span>
    </div>
    <p class="front-url">www.brimoutreachpartners.com</p>
  </section>

  <section class="card card-back">
    <div class="back-logo">
      <span class="dot"></span>
      <span class="name">BRIM Outreach Partners</span>
    </div>
    <div class="back-divider"></div>
    <div class="back-info">
      <p class="person-name">Daniel Marlow-Hayes</p>
      <p class="person-title">Managing Partner</p>
      <p class="location">Denver, CO based (Mtn)</p>
      <ul class="contact-list">
        <li>
          <svg viewBox="0 0 10 10"><path d="M2 0.5 L3.6 2.6 L2.8 3.6 Q4 6 6.4 7.2 L7.4 6.4 L9.5 8 L8.4 9.5 Q3 9 0.5 1.6 Z"/></svg>
          +1-720-555-0142
        </li>
        <li>
          <svg viewBox="0 0 10 10"><path d="M0 2 H10 V8.5 H0 Z M0.6 2.4 L5 5.8 L9.4 2.4" stroke="#4db3e6" stroke-width="0.8"/></svg>
          info@brimoutreachpartners.com
        </li>
        <li>
          <svg viewBox="0 0 10 10"><circle cx="5" cy="5" r="4.6"/></svg>
          brimoutreachpartners.com
        </li>
      </ul>
    </div>
  </section>
</main>
</body>
</html>
```